Menu for Coffee Shop / Restaurant

we are looking for someone to redesign our menus. would like something clean and modern, not too over the top. The business is a coffee shop during the day and transitions to a bar/restaurant in the evenings, so we need a design versatile enough to be used on everything from breakfast menus to cocktail menus. i've attached logo files as well as the current menu files. We're looking to do one menu each for breakfast, brunch (served only on weekends), one that combines the items listed on the attached lunch and dinner menus, and a dessert menu.

Industry/Entity Type

Business

Colors

Designer to choose colors to be used in the design.

Requirements
Must have
• 4 menus : breakfast, brunch, regular food service (combine lunch and dinner menus) and a dessert menu
Nice to have
• would prefer that each menu fit on 1 page, not double sided. We're ok with using legal size paper in order to accomodate

```html
<!DOCTYPE html>
<html lang="en">
<head>
<meta charset="utf-8">
<title>Ostrelle Menus</title>
<link rel="stylesheet" href="https://fonts.googleapis.com/css2?family=Josefin+Sans:wght@600;700&family=Nunito+Sans:wght@400;600&display=swap">
<style>
  :root {
    --sky: #65cbe9;
    --ink: #1c1c1c;
    --paper: #ffffff;
    --backdrop: #e9e6e2;
    --muted: #3a3a3a;
  }
  * { box-sizing: border-box; margin: 0; padding: 0; }
  html, body { width: 1199px; height: 1200px; overflow: hidden; }
  body {
    position: relative;
    background: var(--backdrop);
    font-family: "Nunito Sans", Arial, sans-serif;
    color: var(--ink);
  }
  .menu {
    position: absolute;
    width: 538px;
    height: 761px;
    background: var(--paper);
    box-shadow: 0 4px 14px rgba(0,0,0,0.18);
  }
  .menu--breakfast { left: 37px; top: 32px; }
  .menu--brunch { left: 616px; top: 403px; }
  .menu > * { position: absolute; }

  .brand {
    font-family: "Josefin Sans", Arial, sans-serif;
    font-weight: 700;
    color: var(--sky);
    font-size: 46px;
    letter-spacing: 0.14em;
    line-height: 1;
  }
  .menu-title {
    font-family: "Josefin Sans", Arial, sans-serif;
    font-weight: 700;
    font-size: 15px;
    letter-spacing: 0.5em;
  }
  .heading {
    font-family: "Josefin Sans", Arial, sans-serif;
    font-weight: 700;
    letter-spacing: 0.08em;
    text-transform: uppercase;
    line-height: 1;
  }
  .heading small {
    display: block;
    font-weight: 600;
    font-variant: small-caps;
    text-transform: none;
    letter-spacing: 0.04em;
  }
  .rule { display: block; height: 2px; background: var(--ink); }
  .price {
    font-family: "Josefin Sans", Arial, sans-serif;
    font-weight: 700;
  }
  .item-name {
    font-family: "Josefin Sans", Arial, sans-serif;
    font-weight: 700;
    letter-spacing: 0.06em;
    text-transform: uppercase;
    white-space: nowrap;
  }

  /* build your own */
  .builder {
    left: 25px; top: 142px; width: 487px; height: 209px;
    background: var(--sky);
  }
  .builder > * { position: absolute; }
  .builder__title {
    left: 0; right: 0; top: 14px; text-align: center;
    font-family: "Josefin Sans", Arial, sans-serif;
    font-weight: 700; font-size: 13px; letter-spacing: 0.14em;
  }
  .builder__rule { left: 221px; top: 37px; width: 45px; }
  .builder__col { top: 58px; }
  .builder__col header {
    display: flex; justify-content: space-between; align-items: baseline;
    font-family: "Josefin Sans", Arial, sans-serif; font-weight: 700;
    font-size: 10px; letter-spacing: 0.05em; margin-bottom: 10px;
    white-space: nowrap;
  }
  .builder__col header .price { font-size: 14px; letter-spacing: 0; }
  .builder__col ul { list-style: none; font-size: 9.5px; line-height: 16.3px; }
  .builder__col li::before { content: "• "; }
  .builder__col li.wrap { line-height: 11.5px; padding-top: 2px; }
  .builder__col .note { color: var(--muted); }

  .band { background: var(--sky); }
  .frame { border: 2px solid var(--ink); }

  /* breakfast lists */
  .b-sandwich .heading, .b-omelets .heading { font-size: 15px; }
  .b-sandwich .heading small, .b-omelets .heading small { font-size: 9px; }
  .b-entry { width: 164px; }
  .b-entry .item-name { font-size: 9.5px; margin-bottom: 3px; }
  .b-entry p { font-size: 7.6px; line-height: 9.6px; }
  .b-price { font-size: 13px; }
  .o-entry { width: 170px; }
  .o-entry .price { font-size: 17px; display: block; margin-bottom: 5px; }
  .o-entry .item-name { font-size: 9.5px; margin-bottom: 3px; }
  .o-entry p { font-size: 7.6px; line-height: 9.6px; }

  /* brunch lists */
  .r-entry { width: 126px; }
  .r-entry .item-name { font-size: 11.5px; line-height: 11px; letter-spacing: 0.03em; margin-bottom: 6px; }
  .r-entry p { font-size: 9.4px; line-height: 12px; text-align: justify; }
  .r-price { font-size: 15px; }
  .ro-entry { width: 134px; }
  .ro-entry .price { font-size: 21px; display: block; margin-bottom: 5px; }
  .ro-entry .item-name { font-size: 11.5px; line-height: 11px; letter-spacing: 0.03em; margin-bottom: 3px; }
  .ro-entry p { font-size: 9.4px; line-height: 12px; text-align: justify; }
</style>
</head>
<body>

<section class="menu menu--breakfast">
  <h1 class="brand" style="left:57px;top:38px;">OSTRELLE</h1>
  <h2 class="menu-title" style="left:57px;top:95px;">BREAKFAST</h2>

  <div class="builder">
    <h3 class="builder__title">BUILD YOUR OWN BREAKFAST SANDWICH</h3>
    <span class="rule builder__rule"></span>
    <div class="builder__col" style="left:20px;width:164px;">
      <header><span>CHOOSE YOUR BREAD</span><span class="price">$2.50</span></header>
      <ul>
        <li>Bagels <span class="note">(daily selection)</span></li>
        <li>Brioche Roll</li>
        <li>Brioche Toast</li>
        <li>Ciabatta Rolls</li>
        <li>Croissant <span class="note">(add $1.00)</span></li>
        <li class="wrap">Gluten Free bagel<br>&nbsp;&nbsp;<span class="note">(add $1.00)</span></li>
      </ul>
    </div>
    <div class="builder__col" style="left:208px;width:116px;">
      <header><span>ADD CHEESE</span><span class="price">$1.00</span></header>
      <ul>
        <li>American</li>
        <li>Cheddar</li>
        <li>Pepper Jack</li>
        <li>Swiss</li>
        <li>Cream Cheese</li>
        <li class="wrap">Flavor Cream Cheese<br>&nbsp;&nbsp;<span class="note">(add $0.50)</span></li>
      </ul>
    </div>
    <div class="builder__col" style="left:346px;width:121px;">
      <header><span>ADD PROTEIN</span><span class="price">$1.00</span></header>
      <ul>
        <li>Bacon</li>
        <li>Egg</li>
        <li>Turkey Bacon</li>
        <li>Pork Roll</li>
        <li>Sausage</li>
        <li>Avocado</li>
      </ul>
    </div>
  </div>

  <div class="band" style="left:0;top:416px;width:278px;height:276px;"></div>
  <div class="frame" style="left:218px;top:369px;width:294px;height:371px;"></div>

  <div class="b-sandwich" style="left:52px;top:447px;">
    <h3 class="heading">Sandwich<small>Served with home fries or fruits</small></h3>
  </div>
  <span class="rule" style="left:46px;top:476px;width:45px;"></span>

  <article class="b-entry" style="left:52px;top:506px;">
    <h4 class="item-name">EBLT</h4>
    <p>Fried egg, crispy bacon, arugula, tomato, and mayonnaise on brioche roll.</p>
  </article>
  <span class="price b-price" style="left:231px;top:502px;">$7.95</span>

  <article class="b-entry" style="left:52px;top:564px;">
    <h4 class="item-name">Smoked Salmon Sandwich</h4>
    <p>Sliced smoked salmon, cream cheese, red onion, lettuce, and tomato between a soft toasted brioche roll.</p>
  </article>
  <span class="price b-price" style="left:229px;top:560px;">$11.95</span>

  <article class="b-entry" style="left:52px;top:632px;">
    <h4 class="item-name">Breakfast Burger</h4>
    <p>Angus Beef, sausage patty, cheddar cheese, caramelized onions, lettuce and tomato on toasted brioche roll.</p>
  </article>
  <span class="price b-price" style="left:229px;top:628px;">$13.95</span>

  <div class="b-omelets" style="left:314px;top:396px;">
    <h3 class="heading">Omelets<small>Served with home fries or fruits</small></h3>
  </div>
  <span class="rule" style="left:314px;top:432px;width:45px;"></span>

  <article class="o-entry" style="left:314px;top:455px;">
    <span class="price">$9.95</span>
    <h4 class="item-name">Egg White Omelet</h4>
    <p>Marinated chicken breast and broccoli stuffed.</p>
  </article>
  <article class="o-entry" style="left:314px;top:517px;">
    <span class="price">$9.95</span>
    <h4 class="item-name">Vegetable Omelet</h4>
    <p>Mushrooms, peppers, red onion, spinach, and cheddar cheese.</p>
  </article>
  <article class="o-entry" style="left:314px;top:588px;">
    <span class="price">$9.95</span>
    <h4 class="item-name">Chicken Omelet</h4>
    <p>Marinated chicken breast, spinach, tomato, caramelized onions, and pepper jack cheese.</p>
  </article>
  <article class="o-entry" style="left:314px;top:659px;">
    <span class="price">$11.95</span>
    <h4 class="item-name">Smoked Salmon Omelet</h4>
    <p>Green onions, red peppers, cream cheese, and sliced smoked salmon stuffed inside an omelet.</p>
  </article>
</section>

<section class="menu menu--brunch">
  <h1 class="brand" style="left:58px;top:46px;">OSTRELLE</h1>
  <h2 class="menu-title" style="left:58px;top:110px;">BRUNCH</h2>

  <div class="band" style="left:37px;top:186px;width:248px;height:534px;"></div>
  <div class="frame" style="left:218px;top:145px;width:285px;height:543px;"></div>

  <div style="left:64px;top:214px;">
    <h3 class="heading" style="font-size:17px;">Entrees<small style="font-size:9.5px;">Home fries, fruits or salad.</small></h3>
  </div>
  <span class="rule" style="left:64px;top:247px;width:52px;"></span>

  <article class="r-entry" style="left:64px;top:288px;">
    <h4 class="item-name">Double Take</h4>
    <p>Two eggs any style, two pieces of bacon, two pieces of toast.</p>
  </article>
  <span class="price r-price" style="left:232px;top:285px;">$8.95</span>

  <article class="r-entry" style="left:64px;top:363px;">
    <h4 class="item-name">Bourbon Apple<br>French Toast</h4>
    <p>Thick cut brioche bread, bourbon caramelized apples orange cream cheese and cinnamon brownsugar.</p>
  </article>
  <span class="price r-price" style="left:231px;top:361px;">$9.95</span>

  <article class="r-entry" style="left:64px;top:462px;">
    <h4 class="item-name">Classic Eggs<br>Benedict</h4>
    <p>Traditional Canadian bacon and two poached eggs over a toasted English muffin and buttery Hollandaise on top.</p>
  </article>
  <span class="price r-price" style="left:230px;top:451px;">$12.95</span>

  <article class="r-entry" style="left:64px;top:561px;">
    <h4 class="item-name">Breakfast Burger</h4>
    <p>Angus Beef, sausage patty, cheddar cheese, caramelized onions, lettuce and tomato on toasted brioche roll.</p>
  </article>
  <span class="price r-price" style="left:230px;top:557px;">$14.95</span>

  <article class="r-entry" style="left:64px;top:649px;">
    <h4 class="item-name">Steak &amp; Eggs</h4>
    <p>Grilled Skirt steak and two eggs sunny side up.</p>
  </article>
  <span class="price r-price" style="left:230px;top:645px;">$15.95</span>

  <div style="left:325px;top:178px;">
    <h3 class="heading" style="font-size:17px;">Omelets<small style="font-size:8.5px;">Served with home fries and toast.</small></h3>
  </div>
  <span class="rule" style="left:326px;top:211px;width:52px;"></span>

  <article class="ro-entry" style="left:326px;top:252px;">
    <span class="price">$9.95</span>
    <h4 class="item-name">Egg White Omelet</h4>
    <p>Marinated chicken breast and broccoli.</p>
  </article>
  <article class="ro-entry" style="left:326px;top:332px;">
    <span class="price">$10.95</span>
    <h4 class="item-name">Vegetable Omelet</h4>
    <p>Mushrooms, peppers, red onion, spinach, and cheddar cheese.</p>
  </article>
  <article class="ro-entry" style="left:326px;top:424px;">
    <span class="price">$12.95</span>
    <h4 class="item-name">Chicken Omelet</h4>
    <p>Marinated chicken breast, spinach, tomato, caramelized onions, and pepper jack cheese.</p>
  </article>
  <article class="ro-entry" style="left:326px;top:528px;">
    <span class="price">$13.95</span>
    <h4 class="item-name">Smoked Salmon<br>Omelet</h4>
    <p>Green onions, red peppers, cream cheese, and sliced smoked salmon.</p>
  </article>
</section>

</body>
</html>
```